Webdesign für Hunde- und Katzenernährungsberatung
Zielgruppe
Hunde und Katzenernährungsberatung, für Menschen, die auch bei ihren Hunden und Katzen auf gesunde, natürliche Ernährung achten wollen, ohne unnötigen Geschmacksverstärker, Zucker, Zusatzstoffe, etc. die gesundheitliche Probleme bei den Tieren verursachen können.
Umstellung auf natürliche, artgerechte Fütterung, teils roh, teils gekocht, angepasst auf Grösse, Rasse, Alter etc., auch speziell für Welpen
Beratung bei:
Übergewicht
Allergien
Unverträglichkeiten
Magen-Darm Problemen
individuelle Ernährungspläne
Selbsthergestellte Kekse, Leckerlies, Snacks, Pralinen und div. Hausmannskost in Einmachgläsern (alles auf Vorbestellung).
Diverse Accessoires
Halsbänder, Leinen, Geschirr aus div. natürlichen Materialien
Lern- und Spielzeug aus Holz und Stoff
div. Zubehör für Tiere, sowie auch für Frauchen und Herrchen
Aufgabenstellung
Die Seite sollte stilvoll aber nicht überfüllt sein und im Retro/Vintage Stil gehalten werden, da das Logo bereits sehr wirksam und eher auffällig ist, dezente Töne im Hintergrund, die Nahrungsmittel werden dann ev. auf Schieferplatten oder unauffälligem Hintergrund platziert. Ich sollte zu einem späteren Zeitpunkt selber Fotos, Links, Texte, etc. einfach dazu fügen können.

```html
<!DOCTYPE html>
<html lang="de">
<head>
<meta charset="utf-8">
<title>Pfoten Napf Haus – Ernährungsberatung für Hund und Katze</title>
<link href="https://fonts.googleapis.com/css2?family=Montserrat:wght@400;600;700&family=Sriracha&display=swap" rel="stylesheet">
<style>
:root{
  --sky:#8fbad6;
  --sky-deep:#7aa3bf;
  --slate:#6f93ab;
  --orange:#c7711c;
  --brown:#3f2a1c;
  --paper:#f5f5f5;
  --white:#ffffff;
  --text:#6c6c6c;
  --canvas:#e6e6e6;
}
*{box-sizing:border-box;margin:0;padding:0}
html,body{width:1200px;height:3000px;overflow:hidden}
body{background:radial-gradient(ellipse at 50% 20%,#f1f1f1,var(--canvas) 70%);font-family:'Montserrat',sans-serif;color:var(--text)}
.page{position:absolute;left:156px;top:0;width:887px;height:3000px;background:var(--paper);overflow:hidden}
.abs{position:absolute}
.script{font-family:'Sriracha',cursive;font-weight:400}
.para{font-size:6.6px;line-height:11.4px;color:var(--text)}
.btn{position:absolute;height:17px;color:var(--white);font-size:6.5px;font-weight:700;text-transform:uppercase;display:flex;align-items:center;justify-content:center;letter-spacing:.2px}
.btn--slate{background:var(--slate)}
.btn--orange{background:var(--orange)}
.ph{position:absolute}

/* header */
.site-header{position:absolute;left:0;top:0;width:887px;height:47px;background:var(--white);box-shadow:0 1px 3px rgba(0,0,0,.08);z-index:3}
.brand-tab{position:absolute;left:26px;top:0;width:84px;height:80px;background:var(--white);border-radius:0 0 42px 42px;z-index:3;display:flex;flex-direction:column;align-items:center;padding-top:8px}
.brand-tab .brand-name{font-size:17px;font-weight:700;color:var(--slate);letter-spacing:1px}
.brand-tab .brand-dot{width:40px;height:40px;border-radius:50%;border:2px solid var(--slate);margin-top:3px}
.main-nav{position:absolute;left:375px;top:22px;display:flex;font-size:6.4px;font-weight:700;text-transform:uppercase;color:var(--brown)}
.main-nav span{padding:0 4px;border-left:1px solid #ccc}
.main-nav span:first-child{border-left:0;color:var(--orange)}

/* hero */
.hero{position:absolute;left:0;top:47px;width:887px;height:287px;background:radial-gradient(ellipse at 60% 45%,#a0c6df,var(--sky) 70%);border-bottom:2px solid #e7a55a}
.hero-title{position:absolute;left:194px;top:78px;width:250px;font-size:34px;line-height:31px;color:var(--brown)}
.hero-line{position:absolute;height:2px;background:var(--white);border-radius:2px}
.hero-sub{position:absolute;left:200px;top:155px;font-size:5.8px;color:var(--brown);text-transform:uppercase}
.hero-mark{position:absolute;left:456px;top:11px;width:238px;text-align:center;color:var(--white);font-size:64px;font-weight:700;letter-spacing:4px;line-height:64px}
.hero-ring{position:absolute;left:472px;top:78px;width:192px;height:192px;border-radius:50%;border:5px solid var(--white);background:rgba(255,255,255,.18)}
.hero-arrow{position:absolute;top:128px}

/* welcome */
.portrait{left:164px;top:352px;width:214px;height:306px;border-radius:8px;background:linear-gradient(180deg,#d9cdbd 0%,#b9ab9a 45%,#8d8d93 100%)}
.welcome-title{left:407px;top:398px;font-size:23px;line-height:23px;color:var(--orange)}
.advice-title{left:407px;top:515px;font-size:18px;color:var(--orange)}
.advice-list{left:407px;top:543px;font-size:8.4px;line-height:15px;text-transform:uppercase;color:#555}
.advice-list b{color:var(--orange);font-weight:600;padding:0 3px}

.nutrition-title{left:187px;top:720px;font-size:23px;color:var(--orange)}
.pets-dog{left:460px;top:660px;width:427px;height:490px;border-radius:10px 0 0 10px;background:linear-gradient(160deg,#ece6de 0%,#d9c1a2 55%,#e9e5e0 100%)}
.pets-cat{left:0;top:915px;width:440px;height:230px;border-radius:0 10px 10px 0;background:linear-gradient(160deg,#e9e1d7 0%,#d7c6b4 60%,#e6e3df 100%)}

/* bands */
.band{position:absolute;left:0;width:887px;background:var(--sky)}
.scallop-top{position:absolute;left:0;top:0;width:887px;height:12px;background:radial-gradient(circle at 50% 0,var(--paper) 6.5px,transparent 7px) repeat-x;background-size:14px 12px}
.scallop-bottom{position:absolute;left:0;bottom:0;width:887px;height:12px;background:radial-gradient(circle at 50% 100%,var(--paper) 6.5px,transparent 7px) repeat-x;background-size:14px 12px}
.homemade{top:1194px;height:321px;background:radial-gradient(ellipse at 32% 45%,#b3d3e8,var(--sky) 55%)}
.chihuahua{left:150px;top:1206px;width:280px;height:370px;border-radius:10px;background:linear-gradient(180deg,#dcc4a4 0%,#c9a57a 50%,#b98e5d 100%)}
.homemade-title{left:450px;top:1242px;font-size:23px;color:var(--white)}
.homemade-text{left:450px;top:1284px;width:255px;color:var(--white)}
.shop-sub{left:450px;top:1344px;font-size:14px;color:var(--white)}
.tick-list{left:450px;top:1372px;list-style:none;font-size:6.4px;font-weight:700;color:var(--white);text-transform:uppercase;line-height:11.6px}
.tick-list li{display:flex;align-items:center;gap:5px}

.accessories-title{left:187px;top:1594px;font-size:23px;color:var(--orange)}
.acc-list{left:187px;top:1733px;font-size:6.4px;font-weight:700;color:var(--orange);text-transform:uppercase;line-height:11.6px}
.scratcher{left:470px;top:1549px;width:360px;height:270px;border-radius:10px;background:linear-gradient(160deg,#d9d4d0 0%,#cfb7c9 50%,#b8ded8 100%)}

/* shop */
.shop{top:1876px;height:809px;background:radial-gradient(ellipse at 50% 45%,#a4cae2,var(--sky) 60%)}
.shop-title{left:0;top:1888px;width:887px;text-align:center;font-size:23px;color:var(--white)}
.shop-filter{left:0;top:1928px;width:887px;text-align:center;font-size:6.2px;font-weight:700;color:var(--white);text-transform:uppercase}
.shop-filter span{padding:0 5px}
.card{position:absolute;width:119px;height:195px;background:var(--white);box-shadow:0 1px 3px rgba(0,0,0,.12);text-align:center}
.card-img{position:absolute;left:15px;top:10px;width:89px;height:58px;border-radius:6px;background:linear-gradient(180deg,#e7c9a8,#c98a4e)}
.card-name{position:absolute;left:0;top:82px;width:119px;font-size:6.2px;font-weight:700;color:var(--orange);text-transform:uppercase}
.card-desc{position:absolute;left:8px;top:95px;width:103px;font-size:5.4px;line-height:7.6px;color:var(--text)}
.card-rule{position:absolute;left:10px;top:134px;width:99px;border-top:1px dotted #e0a060}
.card-price{position:absolute;left:0;top:137px;width:119px;font-size:22px;font-weight:700;color:var(--orange);line-height:24px}
.card-meta{position:absolute;left:0;top:162px;width:119px;font-size:4.8px;line-height:6.4px;color:var(--text)}
.card-meta em{font-style:normal;color:var(--orange)}
.card .btn{left:13px;top:183px;width:93px;height:15px;font-size:6px}

/* newsletter */
.newsletter{position:absolute;left:0;top:2685px;width:887px;height:38px;background:var(--sky-deep)}
.nl-input{position:absolute;left:187px;top:9px;width:161px;height:18px;background:var(--white);font-size:6px;color:#aaa;padding:5px 7px}
.nl-text{position:absolute;left:363px;top:8px;width:255px;color:var(--white);font-size:9.4px;white-space:nowrap}
.nl-text small{display:block;font-size:5.4px;margin-top:1px}
.nl-btn{position:absolute;left:626px;top:9px;width:74px;height:18px;background:var(--white);color:var(--slate);font-size:6.2px;font-weight:700;display:flex;align-items:center;justify-content:center}

/* contact */
.contact-brand{left:194px;top:2762px;width:73px;display:flex;flex-direction:column;align-items:center}
.contact-brand .brand-name{font-size:17px;font-weight:700;color:var(--slate);letter-spacing:1px}
.contact-brand .brand-dot{width:44px;height:44px;border-radius:50%;border:2px solid var(--slate);margin-top:2px}
.address{left:187px;top:2848px;font-size:5.6px;line-height:8.4px;color:#555}
.web{left:187px;top:2898px;font-size:5.8px;line-height:8.6px;color:var(--orange);font-weight:600}
.social{left:187px;top:2930px;display:flex;gap:16px}
.social span{width:14px;height:14px;border-radius:50%;background:#7b8a96}
.contact-title{left:363px;top:2752px;font-size:23px;color:var(--orange)}
.contact-sub{left:363px;top:2782px;font-size:5.8px;color:#555}
.field{position:absolute;border-bottom:1px solid #cfcfcf;font-size:5.4px;color:#999;text-transform:uppercase;height:12px}
.field--active{border-bottom-color:var(--orange);color:var(--orange)}
.copy{left:363px;top:2926px;font-size:5.6px;color:#555;display:flex;align-items:center;gap:4px}
.copy i{width:6px;height:6px;background:#888;display:inline-block}

/* footer */
.site-footer{position:absolute;left:0;top:2974px;width:887px;height:26px;background:var(--sky-deep);color:var(--white);font-size:5.6px}
.site-footer .legal{position:absolute;left:187px;top:10px}
.site-footer nav{position:absolute;right:187px;top:10px;text-transform:uppercase}
.site-footer nav span{padding:0 4px;border-left:1px solid rgba(255,255,255,.6)}
.site-footer nav span:first-child{border-left:0}
</style>
</head>
<body>
<div class="page">

  <header class="site-header">
    <nav class="main-nav">
      <span>Startseite</span><span>Ernährungsberatung</span><span>Futter</span><span>Accessories</span><span>Onlineshop</span><span>Kontakt</span>
    </nav>
  </header>
  <div class="brand-tab"><span class="brand-name">PNH</span><span class="brand-dot"></span></div>

  <section class="hero">
    <div class="hero-line" style="left:225px;top:78px;width:170px;transform:rotate(-2deg)"></div>
    <h1 class="hero-title script">Lorem ipsum dolor sit amet</h1>
    <p class="hero-sub">Lorem ipsum dolor sit amet consectetur adipiscing elit</p>
    <div class="hero-line" style="left:225px;top:170px;width:150px;transform:rotate(1deg)"></div>
    <div class="btn btn--slate" style="left:267px;top:191px;width:91px">Online Shop</div>
    <svg class="abs" style="left:405px;top:165px" width="70" height="75" viewBox="0 0 70 75"><path d="M60 4 C20 10 10 40 30 62 C36 68 44 70 50 68" fill="none" stroke="#fff" stroke-width="1.5"/><path d="M44 63 L51 68 L45 73" fill="none" stroke="#fff" stroke-width="1.5"/></svg>
    <div class="hero-mark">PNH</div>
    <div class="hero-ring" role="img" aria-label="Illustration: Hund und Katze mit Futternapf"></div>
    <svg class="hero-arrow" style="left:14px" width="12" height="16" viewBox="0 0 12 16"><path d="M10 1 L2 8 L10 15" fill="none" stroke="#5f7f95" stroke-width="3"/></svg>
    <svg class="hero-arrow" style="left:861px" width="12" height="16" viewBox="0 0 12 16"><path d="M2 1 L10 8 L2 15" fill="none" stroke="#fff" stroke-width="3"/></svg>
  </section>

  <div class="ph portrait" role="img" aria-label="Foto: Ernährungsberaterin mit verschränkten Armen"></div>
  <h2 class="abs welcome-title script">Willkommen auf<br>unserer Website</h2>
  <p class="abs para" style="left:407px;top:451px;width:255px">Lorem ipsum dolor sit amet, consectetur adipiscing elit, sed do eiusmod tempor incididunt ut labore et dolore magna aliqua. Ut enim ad minim veniam, quis nostrud exercitation ullamco laboris nisi ut aliquip ex ea commodo consequat. Duis aute irure dolor in reprehenderit in voluptate velit esse cillum dolore eu fugiat nulla pariatur.</p>
  <h3 class="abs advice-title script">Beratung bei:</h3>
  <p class="abs advice-list">Übergewicht<b>|</b>Allergien<b>|</b>Unverträglichkeiten<br>Magen-Darm Problemen<b>|</b>Individuelle Ernährungspläne</p>
  <p class="abs para" style="left:407px;top:580px;width:255px">Lorem ipsum dolor sit amet, consectetur adipiscing elit, sed do eiusmod tempor incididunt ut labore et dolore magna aliqua. Ut enim ad minim veniam, quis nostrud exercitation ullamco laboris nisi ut aliquip ex ea commodo consequat.</p>

  <div class="ph pets-dog" role="img" aria-label="Foto: Beagle frisst aus einem Metallnapf"></div>
  <div class="ph pets-cat" role="img" aria-label="Foto: Katze frisst aus einem Metallnapf"></div>
  <h2 class="abs nutrition-title script">Ernährungsberatung</h2>
  <p class="abs para" style="left:187px;top:756px;width:255px">Lorem ipsum dolor sit amet, consectetur adipiscing elit, sed do eiusmod tempor incididunt ut labore et dolore magna aliqua. Ut enim ad minim veniam, quis nostrud exercitation ullamco laboris nisi ut aliquip ex ea commodo consequat. Duis aute irure dolor in reprehenderit in voluptate velit esse cillum dolore eu fugiat nulla pariatur.</p>
  <p class="abs para" style="left:187px;top:827px;width:255px">Lorem ipsum dolor sit amet, consectetur adipiscing elit, sed do eiusmod tempor incididunt ut labore et dolore magna aliqua.</p>
  <div class="btn btn--orange" style="left:187px;top:867px;width:91px">Mehr Infos</div>

  <section class="band homemade">
    <div class="scallop-top"></div>
    <div class="scallop-bottom"></div>
  </section>
  <div class="ph chihuahua" role="img" aria-label="Foto: Chihuahua mit Napf im Maul hinter selbstgebackenen Hundekeksen"></div>
  <h2 class="abs homemade-title script">Hausgemachte Tiernahrung</h2>
  <p class="abs para homemade-text">Lorem ipsum dolor sit amet, consectetur adipiscing elit, sed do eiusmod tempor incididunt ut labore et dolore magna aliqua. Ut enim ad minim veniam, quis nostrud exercitation ullamco laboris nisi ut aliquip ex ea commodo consequat. Duis aute irure dolor in reprehenderit in voluptate velit esse cillum dolore eu fugiat nulla pariatur.</p>
  <h3 class="abs shop-sub script">Sie können in unserem Online-Shop</h3>
  <ul class="abs tick-list">
    <li><svg width="8" height="6" viewBox="0 0 8 6"><path d="M1 3 L3 5 L7 1" fill="none" stroke="#fff" stroke-width="1"/></svg>Selbsthergestellte Kekse</li>
    <li><svg width="8" height="6" viewBox="0 0 8 6"><path d="M1 3 L3 5 L7 1" fill="none" stroke="#fff" stroke-width="1"/></svg>Leckerlies</li>
    <li><svg width="8" height="6" viewBox="0 0 8 6"><path d="M1 3 L3 5 L7 1" fill="none" stroke="#fff" stroke-width="1"/></svg>Snacks</li>
    <li><svg width="8" height="6" viewBox="0 0 8 6"><path d="M1 3 L3 5 L7 1" fill="none" stroke="#fff" stroke-width="1"/></svg>Pralinen</li>
    <li><svg width="8" height="6" viewBox="0 0 8 6"><path d="M1 3 L3 5 L7 1" fill="none" stroke="#fff" stroke-width="1"/></svg>Div. Hausmannskost in Einmachgläsern</li>
  </ul>
  <div class="btn btn--slate" style="left:450px;top:1442px;width:91px">Mehr Infos</div>

  <div class="ph scratcher" role="img" aria-label="Foto: Katze auf einem gemusterten Kratzmöbel aus Karton"></div>
  <h2 class="abs accessories-title script">Accessories</h2>
  <p class="abs para" style="left:187px;top:1630px;width:255px">Lorem ipsum dolor sit amet, consectetur adipiscing elit, sed do eiusmod tempor incididunt ut labore et dolore magna aliqua. Ut enim ad minim veniam, quis nostrud exercitation ullamco laboris nisi ut aliquip ex ea commodo consequat. Duis aute irure dolor in reprehenderit in voluptate velit esse cillum dolore eu fugiat nulla pariatur.</p>
  <p class="abs para" style="left:187px;top:1700px;width:255px">Lorem ipsum dolor sit amet, consectetur adipiscing elit, sed do eiusmod tempor incididunt ut labore et dolore magna aliqua.</p>
  <p class="abs acc-list">Halsbänder<br>Leinen<br>Geschirr aus div. natürlichen Materialien<br>Lern- und Spielzeug aus Holz und Stoff<br>Div. Zubehör für Tiere</p>
  <div class="btn btn--slate" style="left:187px;top:1802px;width:91px">Mehr Infos</div>

  <section class="band shop">
    <div class="scallop-top"></div>
  </section>
  <h2 class="abs shop-title script">Online Shop</h2>
  <p class="abs shop-filter"><span>All Items</span>|<span>Food</span>|<span>Snacks</span>|<span>Pralinen</span>|<span>Accessories</span></p>

  <article class="card" style="left:187px;top:1954px"><div class="card-img" role="img" aria-label="Foto: Trockenfutter"></div><h4 class="card-name">Product name goes here</h4><p class="card-desc">Lorem ipsum dolor sit amet, consectetur adipiscing elit, sed do eiusmod tempor incididunt ut labore et dolore magna aliqua.</p><div class="card-rule"></div><p class="card-price">€ 10,50</p><p class="card-meta">inkl. 19% MwSt. zzgl.<br><em>Versandkosten</em> | Lieferzeit 2 - 3 tage</p><div class="btn btn--orange">Add to cart</div></article>
  <article class="card" style="left:319px;top:1954px"><div class="card-img" role="img" aria-label="Foto: Trockenfutter"></div><h4 class="card-name">Product name goes here</h4><p class="card-desc">Lorem ipsum dolor sit amet, consectetur adipiscing elit, sed do eiusmod tempor incididunt ut labore et dolore magna aliqua.</p><div class="card-rule"></div><p class="card-price">€ 10,50</p><p class="card-meta">inkl. 19% MwSt. zzgl.<br><em>Versandkosten</em> | Lieferzeit 2 - 3 tage</p><div class="btn btn--slate">Add to cart</div></article>
  <article class="card" style="left:451px;top:1954px"><div class="card-img" role="img" aria-label="Foto: Trockenfutter"></div><h4 class="card-name">Product name goes here</h4><p class="card-desc">Lorem ipsum dolor sit amet, consectetur adipiscing elit, sed do eiusmod tempor incididunt ut labore et dolore magna aliqua.</p><div class="card-rule"></div><p class="card-price">€ 10,50</p><p class="card-meta">inkl. 19% MwSt. zzgl.<br><em>Versandkosten</em> | Lieferzeit 2 - 3 tage</p><div class="btn btn--slate">Add to cart</div></article>
  <article class="card" style="left:583px;top:1954px"><div class="card-img" role="img" aria-label="Foto: Trockenfutter"></div><h4 class="card-name">Product name goes here</h4><p class="card-desc">Lorem ipsum dolor sit amet, consectetur adipiscing elit, sed do eiusmod tempor incididunt ut labore et dolore magna aliqua.</p><div class="card-rule"></div><p class="card-price">€ 10,50</p><p class="card-meta">inkl. 19% MwSt. zzgl.<br><em>Versandkosten</em> | Lieferzeit 2 - 3 tage</p><div class="btn btn--slate">Add to cart</div></article>

  <article class="card" style="left:187px;top:2181px"><div class="card-img" role="img" aria-label="Foto: Trockenfutter"></div><h4 class="card-name">Product name goes here</h4><p class="card-desc">Lorem ipsum dolor sit amet, consectetur adipiscing elit, sed do eiusmod tempor incididunt ut labore et dolore magna aliqua.</p><div class="card-rule"></div><p class="card-price">€ 10,50</p><p class="card-meta">inkl. 19% MwSt. zzgl.<br><em>Versandkosten</em> | Lieferzeit 2 - 3 tage</p><div class="btn btn--slate">Add to cart</div></article>
  <article class="card" style="left:319px;top:2181px"><div class="card-img" role="img" aria-label="Foto: Trockenfutter"></div><h4 class="card-name">Product name goes here</h4><p class="card-desc">Lorem ipsum dolor sit amet, consectetur adipiscing elit, sed do eiusmod tempor incididunt ut labore et dolore magna aliqua.</p><div class="card-rule"></div><p class="card-price">€ 10,50</p><p class="card-meta">inkl. 19% MwSt. zzgl.<br><em>Versandkosten</em> | Lieferzeit 2 - 3 tage</p><div class="btn btn--slate">Add to cart</div></article>
  <article class="card" style="left:451px;top:2181px"><div class="card-img" role="img" aria-label="Foto: Trockenfutter"></div><h4 class="card-name">Product name goes here</h4><p class="card-desc">Lorem ipsum dolor sit amet, consectetur adipiscing elit, sed do eiusmod tempor incididunt ut labore et dolore magna aliqua.</p><div class="card-rule"></div><p class="card-price">€ 10,50</p><p class="card-meta">inkl. 19% MwSt. zzgl.<br><em>Versandkosten</em> | Lieferzeit 2 - 3 tage</p><div class="btn btn--slate">Add to cart</div></article>
  <article class="card" style="left:583px;top:2181px"><div class="card-img" role="img" aria-label="Foto: Trockenfutter"></div><h4 class="card-name">Product name goes here</h4><p class="card-desc">Lorem ipsum dolor sit amet, consectetur adipiscing elit, sed do eiusmod tempor incididunt ut labore et dolore magna aliqua.</p><div class="card-rule"></div><p class="card-price">€ 10,50</p><p class="card-meta">inkl. 19% MwSt. zzgl.<br><em>Versandkosten</em> | Lieferzeit 2 - 3 tage</p><div class="btn btn--slate">Add to cart</div></article>

  <article class="card" style="left:187px;top:2408px"><div class="card-img" role="img" aria-label="Foto: Trockenfutter"></div><h4 class="card-name">Product name goes here</h4><p class="card-desc">Lorem ipsum dolor sit amet, consectetur adipiscing elit, sed do eiusmod tempor incididunt ut labore et dolore magna aliqua.</p><div class="card-rule"></div><p class="card-price">€ 10,50</p><p class="card-meta">inkl. 19% MwSt. zzgl.<br><em>Versandkosten</em> | Lieferzeit 2 - 3 tage</p><div class="btn btn--slate">Add to cart</div></article>
  <article class="card" style="left:319px;top:2408px"><div class="card-img" role="img" aria-label="Foto: Trockenfutter"></div><h4 class="card-name">Product name goes here</h4><p class="card-desc">Lorem ipsum dolor sit amet, consectetur adipiscing elit, sed do eiusmod tempor incididunt ut labore et dolore magna aliqua.</p><div class="card-rule"></div><p class="card-price">€ 10,50</p><p class="card-meta">inkl. 19% MwSt. zzgl.<br><em>Versandkosten</em> | Lieferzeit 2 - 3 tage</p><div class="btn btn--slate">Add to cart</div></article>
  <article class="card" style="left:451px;top:2408px"><div class="card-img" role="img" aria-label="Foto: Trockenfutter"></div><h4 class="card-name">Product name goes here</h4><p class="card-desc">Lorem ipsum dolor sit amet, consectetur adipiscing elit, sed do eiusmod tempor incididunt ut labore et dolore magna aliqua.</p><div class="card-rule"></div><p class="card-price">€ 10,50</p><p class="card-meta">inkl. 19% MwSt. zzgl.<br><em>Versandkosten</em> | Lieferzeit 2 - 3 tage</p><div class="btn btn--slate">Add to cart</div></article>
  <article class="card" style="left:583px;top:2408px"><div class="card-img" role="img" aria-label="Foto: Trockenfutter"></div><h4 class="card-name">Product name goes here</h4><p class="card-desc">Lorem ipsum dolor sit amet, consectetur adipiscing elit, sed do eiusmod tempor incididunt ut labore et dolore magna aliqua.</p><div class="card-rule"></div><p class="card-price">€ 10,50</p><p class="card-meta">inkl. 19% MwSt. zzgl.<br><em>Versandkosten</em> | Lieferzeit 2 - 3 tage</p><div class="btn btn--slate">Add to cart</div></article>

  <div class="btn btn--slate" style="left:385px;top:2642px;width:118px">Load more products</div>

  <section class="newsletter">
    <div class="nl-input">Email Address</div>
    <p class="nl-text">Newsletter anfordern und 5 Euro Gutschein sichern<small>Angebote &amp; Neuigkeiten direkt per E-Mail (Abmeldung jederzeit möglich)</small></p>
    <div class="nl-btn">JETZT ANMELDEN</div>
  </section>

  <div class="abs contact-brand"><span class="brand-name">PNH</span><span class="brand-dot"></span></div>
  <p class="abs address">Company Address will be here<br>00112233 | Country Name will go here<br><br>Fon (0020) 123 44 567 - Fax (0020) 123 44 567</p>
  <p class="abs web">www.pfotennapfhaus.ch<br>info@pfotennapfhaus.ch</p>
  <div class="abs social"><span></span><span></span><span></span><span></span><span></span></div>

  <h2 class="abs contact-title script">Kontaktieren Sie uns jetzt</h2>
  <p class="abs contact-sub">Sie können uns wie folgt erreichen. Wir freuen uns über Ihre Kontakt Anfrage.</p>
  <div class="field field--active" style="left:363px;top:2795px;width:160px">Your Name</div>
  <div class="field" style="left:538px;top:2795px;width:162px">Your Email</div>
  <div class="field" style="left:363px;top:2822px;width:337px">Subject</div>
  <div class="field" style="left:363px;top:2848px;width:337px;height:40px">Your Message</div>
  <p class="abs copy">Send copy to yourself <i></i></p>
  <div class="btn btn--orange" style="left:609px;top:2923px;width:91px">Send Message</div>

  <footer class="site-footer">
    <p class="legal">© 2017 Pfoten Napf Haus - All Rights reserved</p>
    <nav><span>Privacy</span><span>Impressum</span><span>AGB</span><span>Kontakt</span></nav>
  </footer>

</div>
</body>
</html>
```